" Serviço público e privado Formação e qualificação profissional em gestão e Gerenciamento de Projetos Gestão de projetos Mapeamento de processos Mediação de parcerias Inovação tecnológica Suporte de logistica e suprimentos Consultorias técnicas sem limitação de áreas de atuação. Produção de conhecimento Publicações e edições de livros, revistas e periódicos Desenvolvimento de protótipos Desenvolvimento de sistemas, serviços inovadores, aplicativos de inteligência mobile. Construção e gestão de parceria. Construção e desenvolvimento de portfólio de serviços Desenvolvimento e apóio à tecnologias sociais inovadoras Constução, desenvolvimento de planejamento estratégico Assessoria em desenvolvimento institucional integrado Desenvolvimento e aplicação de pesquisas Atuar na área de responsabilidade sócio-ambiental "

```html
<!DOCTYPE html>
<html lang="pt-BR">
<head>
<meta charset="UTF-8">
<title>Norteva Gestão — Pasta institucional</title>
<link rel="stylesheet" href="https://fonts.googleapis.com/css2?family=Montserrat:wght@400;500&display=swap">
<style>
  :root {
    --canvas-bg: #e9eaec;
    --navy-deep: #0f2440;
    --navy: #1b3a5e;
    --navy-light: #2a5079;
    --white: #ffffff;
    --paper: #fbfbfc;
    --paper-shade: #dcdde0;
    --ink-soft: #6b7380;
  }
  * { margin: 0; padding: 0; box-sizing: border-box; }
  html, body { width: 1200px; height: 1200px; overflow: hidden; }
  body {
    background: var(--canvas-bg);
    font-family: "Montserrat", sans-serif;
    display: flex;
    align-items: center;
    justify-content: center;
  }
  .folder-spread {
    display: flex;
    width: 1000px;
    height: 760px;
    box-shadow: 0 18px 40px rgba(15, 36, 64, 0.18);
  }
  .folder-back {
    position: relative;
    width: 500px;
    height: 100%;
    background: linear-gradient(100deg, var(--paper-shade) 0%, var(--paper) 35%, var(--white) 70%, #eef0f2 100%);
    display: flex;
    flex-direction: column;
    justify-content: flex-end;
    align-items: center;
    padding-bottom: 56px;
  }
  .folder-front {
    position: relative;
    width: 500px;
    height: 100%;
    background: linear-gradient(160deg, var(--navy) 0%, var(--navy-deep) 100%);
    display: flex;
    align-items: center;
    justify-content: center;
    overflow: hidden;
  }
  .front-waves {
    position: absolute;
    inset: 0;
    width: 100%;
    height: 100%;
  }
  .brand-name {
    position: relative;
    font-weight: 500;
    letter-spacing: 0.5px;
  }
  .folder-front .brand-name { font-size: 40px; color: var(--white); }
  .folder-back .brand-name { font-size: 20px; color: var(--navy-deep); }
  .contact-list {
    list-style: none;
    margin-top: 14px;
    text-align: center;
    font-size: 8px;
    line-height: 1.6;
    color: var(--ink-soft);
  }
</style>
</head>
<body>
  <main class="folder-spread">
    <section class="folder-back">
      <span class="brand-name">Norteva Gestão</span>
      <ul class="contact-list">
        <li>www.norteva.com.br</li>
        <li>Rua das Flores, 120 – Centro – Cidade – UF – 00000-000</li>
        <li>(11) 0000-0000 | contato@norteva.com.br</li>
      </ul>
    </section>
    <section class="folder-front">
      <svg class="front-waves" viewBox="0 0 500 760" preserveAspectRatio="none" aria-hidden="true">
        <path d="M0 120 C160 60 320 200 500 110 L500 0 L0 0 Z" fill="#2a5079" opacity="0.35"/>
        <path d="M0 210 C180 150 330 260 500 190 L500 150 C330 230 170 110 0 170 Z" fill="#ffffff" opacity="0.06"/>
        <path d="M0 760 L0 640 C160 590 330 700 500 620 L500 760 Z" fill="#0a1a30" opacity="0.4"/>
      </svg>
      <span class="brand-name">Norteva Gestão</span>
    </section>
  </main>
</body>
</html>
```